Business Card Design

We need a business card designed to the point of print ready to take to our printers. the design should be professional, easy to read and simple. The cards should represent our business as professional and trust worthy.

Attached are several versions o the logo, and also the details for the card to be printed. please do communicate if different versions of the logo is required.

Business

```html
<!DOCTYPE html>
<html lang="en">
<head>
<meta charset="utf-8">
<title>RecoverMyFunds Business Card</title>
<link rel="stylesheet" href="https://fonts.googleapis.com/css2?family=Questrial&display=swap">
<style>
  :root {
    --page: #e6e6e4;
    --card: #ffffff;
    --card-shade: #ececec;
    --ink: #5a5a5a;
    --ink-dark: #3c3c3c;
    --accent: #f29a12;
  }
  * { box-sizing: border-box; margin: 0; padding: 0; }
  html, body {
    width: 1200px; height: 871px; overflow: hidden;
    background: var(--page);
    font-family: "Questrial", "Century Gothic", sans-serif;
    color: var(--ink);
  }
  .sheet {
    width: 1200px; height: 871px;
    display: flex; align-items: center; justify-content: center; gap: 60px;
  }
  .card {
    position: relative;
    width: 520px; height: 318px;
    background: linear-gradient(160deg, var(--card) 40%, var(--card-shade) 100%);
    box-shadow: 0 6px 18px rgba(0,0,0,0.18);
  }
  .brand-name {
    color: var(--ink);
    font-weight: 400;
    line-height: 1;
    letter-spacing: -0.5px;
  }
  .brand-name .suffix { display: block; text-align: right; }

  /* front */
  .card-front .brand-name {
    position: absolute; left: 0; right: 0; top: 100px;
    margin: 0 auto; width: max-content;
    font-size: 40px;
  }
  .card-front .brand-name .suffix { font-size: 22px; margin-top: 4px; }
  .card-front .website {
    position: absolute; left: 0; right: 0; top: 228px;
    text-align: center; font-size: 14px; color: var(--accent);
    letter-spacing: 0.3px;
  }

  /* back */
  .card-back .holder {
    position: absolute; left: 34px; top: 74px;
  }
  .holder .person { font-size: 16px; font-weight: 700; color: var(--ink-dark); }
  .holder .role { font-size: 13px; color: var(--accent); margin-top: 2px; }
  .card-back .brand-name {
    position: absolute; right: 34px; top: 52px;
    font-size: 34px;
  }
  .card-back .brand-name .suffix { font-size: 19px; margin-top: 4px; }
  .card-back .rule {
    position: absolute; left: 34px; right: 34px; top: 160px;
    height: 2px; background: var(--accent);
  }
  .contact {
    position: absolute; right: 34px; top: 178px;
    text-align: right; font-size: 14px; color: var(--ink-dark);
    line-height: 1.75;
  }
  .contact .label { color: var(--accent); font-weight: 700; margin-right: 8px; }
</style>
</head>
<body>
  <main class="sheet">
    <section class="card card-front" aria-label="Card front">
      <div class="brand-name">RecoverMyFunds<span class="suffix">Pty Ltd</span></div>
      <p class="website">www.recovermyfunds.com.au</p>
    </section>

    <section class="card card-back" aria-label="Card back">
      <div class="holder">
        <p class="person">Dana Whitford</p>
        <p class="role">Managing Director</p>
      </div>
      <div class="brand-name">RecoverMyFunds<span class="suffix">Pty Ltd</span></div>
      <div class="rule"></div>
      <div class="contact">
        <p class="address">PO Box 2210 Harbour Centre Qld 4551</p>
        <p><span class="label">phone</span>+61 400 555 019</p>
        <p><span class="label">email</span>dwhitford@recovermyfunds.com.au</p>
      </div>
    </section>
  </main>
</body>
</html>
```